Buchcover-Design für Coaching-Buch
Zielgruppe
22 Coaches (m/w/d) haben zusammen ein Buch geschrieben - mit ihren besten Tipps, Mut machenden Geschichten und Inspirationen. Herausgekommen ist 'Die stille Mentorin am Fensterbrett - 22 Schatzkisten lüften ihre Rätsel'. Zielgruppe sind vorwiegend Frauen, häufig mit spirituellem Hintergrund oder an Selbstentwicklung interessiert, sowie Menschen, die sich ermutigen lassen möchten und Menschen, die inspirierende Texte und Geschichten mögen. Die Themen sind ganz unterschiedlich, von Selbstliebe über die Wirkung von Farben, vom Überwinden von Krisen und Angst, Umgang mit Emotionen etc. pp. - ein ganzer Blumenstrauß an Themen.
Aufgabenstellung
Der Titel 'Die stille Mentorin am Fensterbrett' kam auf, weil wir die Vorstellung hatten, dass in dem Buch vielleicht abends im Bett gelesen wird und man dann ruhig schlafen kann.
Warum Füllhörner? Nun, jeder Coach hat viel zu geben. Zu jedem Text wird es ein Geschenk geben, das die Autor*innen online zur Verfügung stellen. Dies sind PDFs mit Tipps, Meditationen oder sogar eine kurze Gratis-Session. Es braucht also etwas auf dem Cover, das darauf hindeutet, vielleicht eine Plakette oder etwas Ähnliches, das 'Mit 22 Geschenken' besagt. Im Buchsatz wird dies durch einen Link (E-Book) und durch einen QR-Code (Print) umgesetzt.

```html
<!DOCTYPE html>
<html lang="de">
<head>
<meta charset="utf-8">
<title>Die stille Mentorin am Fensterbrett – Buchcover</title>
<link rel="stylesheet" href="https://fonts.googleapis.com/css2?family=Lexend:wght@300;400&family=Lato:wght@400&display=swap">
<style>
  :root {
    --backdrop: #e4e4e4;
    --paper: #ffffff;
    --plum: #7b4a6c;
    --rust: #8c4a42;
    --wine: #9a4a5a;
    --violet: #8a6a98;
    --teal: #7fb8b6;
    --badge-text: #ffffff;
  }
  * { box-sizing: border-box; margin: 0; padding: 0; }
  html, body {
    width: 1200px;
    height: 857px;
    overflow: hidden;
    background: var(--backdrop);
  }
  .book-cover {
    position: absolute;
    left: 327px;
    top: 28px;
    width: 546px;
    height: 801px;
    background: linear-gradient(180deg, var(--paper) 60%, #f4f4f4 100%);
    overflow: hidden;
  }
  .cover-artwork {
    position: absolute;
    left: 0;
    top: 122px;
    width: 370px;
    height: 679px;
    background:
      radial-gradient(ellipse 60% 45% at 72% 62%, rgba(127,184,182,0.75) 0%, rgba(127,184,182,0) 70%),
      radial-gradient(ellipse 80% 60% at 35% 55%, rgba(138,106,152,0.85) 0%, rgba(138,106,152,0) 75%),
      linear-gradient(90deg, var(--wine) 0%, rgba(154,74,90,0.6) 18%, rgba(154,74,90,0) 55%);
    border-radius: 0 60% 40% 0 / 0 40% 60% 0;
    opacity: 0.9;
  }
  .cover-title {
    position: absolute;
    right: 46px;
    top: 70px;
    font-family: "Lexend", sans-serif;
    font-weight: 300;
    font-size: 45px;
    line-height: 48px;
    color: var(--plum);
    text-align: right;
    letter-spacing: 0.5px;
  }
  .cover-subtitle {
    position: absolute;
    right: 44px;
    top: 390px;
    font-family: "Lato", sans-serif;
    font-size: 13.5px;
    line-height: 19px;
    letter-spacing: 0.6px;
    text-transform: uppercase;
    color: var(--rust);
    text-align: right;
  }
  .gift-badge {
    position: absolute;
    left: 362px;
    top: 680px;
    width: 200px;
    height: 30px;
    background: var(--plum);
    transform: rotate(-8deg);
    transform-origin: left top;
    color: var(--badge-text);
    font-family: "Lato", sans-serif;
    font-size: 13px;
    line-height: 30px;
    padding-left: 13px;
    letter-spacing: 0.3px;
    text-transform: uppercase;
  }
</style>
</head>
<body>
  <main class="book-cover">
    <div class="cover-artwork" role="img" aria-label="Aquarell-Porträt im Profil mit Farbverlauf von Weinrot über Violett zu Türkis"></div>
    <h1 class="cover-title">Die<br>stille<br>Mentorin<br>am Fenster-<br>brett</h1>
    <p class="cover-subtitle">22 Schatzkisten<br>lüften ihre<br>Rätsel.</p>
    <div class="gift-badge">Mit 22 Geschenken</div>
  </main>
</body>
</html>
```